Zelvrin
business cards & stationery
Project: Zelvrin
Zelvrin -
Creative Brief
Simple
Marcus Holt
VP Sales & Marketing
417 Fenwick Ave. #615-284 Brookmere Falls, NV 89733
temporary@zelvrin-example.com
www.zelvrin-example.com
Your Game, Everywhere

```html
<!DOCTYPE html>
<html lang="en">
<head>
<meta charset="utf-8">
<title>Zelvrin Business Card</title>
<link href="https://fonts.googleapis.com/css2?family=Open+Sans:wght@400;600;700&display=swap" rel="stylesheet">
<style>
  :root {
    --board-top: #000000;
    --board-mid: #1a1d6e;
    --board-bottom: #2160c0;
    --card-front: #ffffff;
    --card-back: #3b3b3b;
    --ink-dark: #6b6b6b;
    --ink-name: #7a7a7a;
    --ink-light: #ffffff;
    --accent: #1d8fe6;
    --label: #ffffff;
  }
  * { margin: 0; padding: 0; box-sizing: border-box; }
  html, body { width: 1200px; height: 931px; overflow: hidden; }
  body {
    position: relative;
    font-family: "Open Sans", Arial, sans-serif;
    background: linear-gradient(to bottom, var(--board-top) 0%, var(--board-top) 22%, var(--board-mid) 62%, var(--board-bottom) 100%);
  }
  .board-label {
    position: absolute;
    left: 0; width: 100%;
    text-align: center;
    color: var(--label);
    font-size: 20px;
  }
  .board-label--front { top: 22px; }
  .board-label--back { top: 862px; }
  .card {
    position: absolute;
    left: 284px;
    width: 647px;
    height: 373px;
    box-shadow: 6px 14px 22px rgba(0,0,0,0.6);
  }
  .card--front { top: 58px; background: var(--card-front); }
  .card--back {
    top: 477px;
    background: var(--card-back);
    background-image: repeating-linear-gradient(45deg, rgba(255,255,255,0.02) 0 2px, rgba(0,0,0,0.02) 2px 4px);
  }
  .person {
    position: absolute;
    left: 37px; top: 70px;
    display: flex; align-items: center;
  }
  .person-name {
    font-weight: 700;
    font-size: 19px;
    letter-spacing: 0.5px;
    color: var(--ink-name);
  }
  .person-title {
    margin-left: 8px;
    padding-left: 8px;
    border-left: 2px solid var(--ink-name);
    font-size: 13px;
    color: var(--ink-dark);
    line-height: 18px;
  }
  .address {
    position: absolute;
    left: 37px; top: 160px;
    font-size: 15px;
    line-height: 22px;
    color: var(--ink-dark);
  }
  .contacts {
    position: absolute;
    left: 37px; top: 210px;
    list-style: none;
    font-size: 15px;
    color: var(--ink-dark);
  }
  .contacts li { display: flex; align-items: center; height: 29px; }
  .contacts svg { width: 15px; height: 15px; margin-right: 10px; fill: var(--ink-dark); }
  .brand {
    position: absolute;
    right: 46px; top: 262px;
    display: flex; align-items: center;
  }
  .brand-name {
    font-weight: 700;
    font-size: 44px;
    letter-spacing: 1px;
    color: var(--ink-dark);
  }
  .brand-dot {
    width: 22px; height: 22px;
    margin-left: 10px;
    border-radius: 50%;
    background: var(--accent);
  }
  .brand-decoration {
    position: absolute;
    left: 20px; top: 50px;
    width: 270px; height: 290px;
    border-radius: 12px;
    background: radial-gradient(circle at 45% 50%, rgba(29,143,230,0.35), rgba(29,143,230,0) 70%);
  }
  .website {
    position: absolute;
    left: 288px; top: 176px;
    font-size: 25px;
    color: var(--ink-light);
  }
</style>
</head>
<body>
  <div class="board-label board-label--front">Bizcard Front</div>

  <section class="card card--front">
    <div class="person">
      <span class="person-name">MARCUS HOLT</span>
      <span class="person-title">VP Sales &amp; Marketing</span>
    </div>
    <div class="address">
      417 Fenwick Ave. #615-284<br>
      Brookmere Falls, NV 89733
    </div>
    <ul class="contacts">
      <li><svg viewBox="0 0 16 16"><path d="M3.5 1l2.5 3-1.5 2c1 2 3 4 5 5l2-1.5 3 2.5-1.5 2.5C7 16 0 9 1 2.5z"/></svg>(111) 111-1111</li>
      <li><svg viewBox="0 0 16 16"><path d="M4 0h8a1 1 0 0 1 1 1v14a1 1 0 0 1-1 1H4a1 1 0 0 1-1-1V1a1 1 0 0 1 1-1zm1 2v10h6V2zm3 11a1 1 0 1 0 0 2 1 1 0 0 0 0-2z"/></svg>(111) 111-1111</li>
      <li><svg viewBox="0 0 16 16"><path d="M3 0h7l4 4v12H3zm2 6v1h7V6zm0 3v1h7V9zm0 3v1h7v-1z"/></svg>(111) 111-1111</li>
      <li><svg viewBox="0 0 16 16"><path d="M0 3h16v10H0zm1 1v.5l7 4.5 7-4.5V4z"/></svg>temporary@zelvrin-example.com</li>
    </ul>
    <div class="brand">
      <span class="brand-name">zelvrin</span>
      <span class="brand-dot"></span>
    </div>
  </section>

  <section class="card card--back">
    <div class="brand-decoration" role="img" aria-label="Zelvrin brand symbol decoration area"></div>
    <div class="website">www.zelvrin-example.com</div>
  </section>

  <div class="board-label board-label--back">Bizcard Back</div>
</body>
</html>
```